Website design for Maple Nook Kidcare

I need a website designed for my daycare business, Maple Nook Kidcare, now that I have a new logo. My former website was ok but simple and I did not have a logo yet. It also was created by me using a template and was entirely pink. I loved the bright, happy feel of it but worried it might not appeal as much to potential clients who have sons. Therefore, I need a site which will appeal to both genders while still keeping the cheerful color scheme of my new logo, which has pinks, blue, green and cream.

Reason: Hello! I am still trying to download my new logo and am sorry it is taking me so long. Hopefully I will it posted by the end of today (US Eastern Standard Time). Thank you all very much for your patience!

Hello! I have finally managed to upload my new logo for you to use in designing my website. I'm sorry it took so long and greatly appreciate your time and creative efforts! I look forward to seeing what is submitted based on my logo design and its style/colors.

Many thanks!

Reason: As I've been traveling and posted my logo file late, I am extending my deadline. I am now back and can focus on providing more and better feedback. I appreciate your patience and submissions very much!

Reason: I need more time to provide feedback and make decisions.

Industry/Entity Type

Daycare

Colors
0192cd
33a6d7
86cae7
cadf82
fbf289
add136
e34197

```html
<!DOCTYPE html>
<html lang="en">
<head>
<meta charset="utf-8">
<title>Maple Nook Kidcare</title>
<link rel="stylesheet" href="https://fonts.googleapis.com/css2?family=Arbutus+Slab&family=Arimo:wght@400&display=swap">
<style>
  :root {
    --sky-top: #eaf6fd;
    --sky-mid: #8fd0f0;
    --sky-low: #5fb6e4;
    --grass: #a6cf52;
    --grass-dark: #7fb33a;
    --panel: #ffffff;
    --nav: #2a8fcf;
    --nav-tail: #1479b8;
    --nav-fold: #0d5f95;
    --heading-green: #8dc63f;
    --text: #555555;
    --news-heading: #444444;
    --card-orange: #f26b3a;
    --card-pink: #e04a72;
    --card-purple: #7c64ad;
    --logo-pink: #e34197;
    --white: #ffffff;
  }
  * { box-sizing: border-box; margin: 0; padding: 0; }
  html, body { width: 1191px; height: 1200px; overflow: hidden; }
  body { position: relative; font-family: "Arimo", Arial, sans-serif; color: var(--text); }

  .scenery {
    position: absolute; inset: 0;
    background: linear-gradient(180deg, var(--sky-top) 0%, var(--sky-mid) 30%, var(--sky-low) 55%, #7cc3e6 68%, var(--grass) 80%, var(--grass-dark) 100%);
  }
  .kids-art { position: absolute; left: 200px; top: 0; width: 240px; height: 156px; background: linear-gradient(180deg, #f7c7d6, #b9ddf2); border-radius: 40px 40px 0 0; opacity: .8; }
  .rainbow-art { position: absolute; left: 730px; top: 4px; width: 350px; height: 153px; background: linear-gradient(180deg, #d9c6ee, #bfe2f5); border-radius: 175px 175px 0 0; opacity: .8; }
  .brand { position: absolute; left: 470px; top: 76px; width: 240px; text-align: center; font-family: "Arbutus Slab", Georgia, serif; font-size: 26px; line-height: 30px; color: var(--logo-pink); }
  .brand-mark { display: block; width: 40px; height: 40px; margin: 0 auto 6px; border-radius: 50%; background: var(--logo-pink); }

  .panel { position: absolute; left: 110px; top: 157px; width: 980px; height: 981px; background: var(--panel); border-radius: 10px; }
  .hero { position: absolute; left: 124px; top: 172px; width: 952px; height: 295px; border-radius: 10px; background: linear-gradient(90deg, #d35a3c 0%, #e9c25a 30%, #3c7fd0 55%, #cfe6f5 75%, #f07a2c 100%); }

  .nav-ribbon { position: absolute; left: 62px; top: 481px; width: 1076px; height: 82px; }
  .nav { position: absolute; left: 93px; top: 481px; width: 1014px; height: 48px; background: var(--nav); border-radius: 6px; display: flex; justify-content: center; align-items: center; gap: 28px; }
  .nav a { font-family: "Arbutus Slab", Georgia, serif; font-size: 18px; color: var(--white); text-decoration: none; }

  .intro { position: absolute; left: 136px; top: 550px; width: 930px; }
  .intro h1 { font-family: "Arbutus Slab", Georgia, serif; font-weight: 400; font-size: 24px; line-height: 29px; color: var(--heading-green); margin-left: 2px; }
  .intro p { font-size: 14px; line-height: 17px; margin-top: 16px; }

  .news { position: absolute; left: 138px; top: 770px; width: 195px; }
  .news h2 { font-family: "Arbutus Slab", Georgia, serif; font-weight: 400; font-size: 24px; color: var(--news-heading); margin-bottom: 16px; }
  .news p { font-size: 14px; line-height: 17px; margin-bottom: 17px; }

  .card { position: absolute; top: 815px; width: 235px; height: 299px; border-radius: 10px; color: var(--white); padding: 50px 24px 0 26px; }
  .card h3 { font-family: "Arbutus Slab", Georgia, serif; font-weight: 400; font-size: 25px; text-align: center; margin-bottom: 6px; letter-spacing: .5px; }
  .card p { font-size: 14px; line-height: 17px; }
  .card-learning { left: 356px; background: var(--card-orange); }
  .card-creativity { left: 601px; background: var(--card-pink); padding-top: 54px; }
  .card-sharing { left: 846px; background: var(--card-purple); padding-top: 54px; }
  .card-art { position: absolute; border-radius: 50%; opacity: .85; }
  .art-learning { left: 390px; top: 722px; width: 165px; height: 118px; background: linear-gradient(135deg, #f4d64e, #e05a4a); }
  .art-creativity { left: 650px; top: 690px; width: 140px; height: 170px; background: linear-gradient(180deg, #b6d9f2, #f49ac0); }
  .art-sharing { left: 896px; top: 710px; width: 150px; height: 135px; background: linear-gradient(135deg, #b5dd6a, #4fa3d8); }

  .footer { position: absolute; left: 116px; top: 1152px; width: 960px; display: flex; justify-content: space-between; font-size: 14px; color: var(--white); }
  .footer a { color: var(--white); text-decoration: none; }
</style>
</head>
<body>
  <div class="scenery" role="img" aria-label="Cartoon sky with clouds, trees, butterflies and rolling green hills"></div>
  <div class="kids-art" role="img" aria-label="Illustration of two cartoon children running"></div>
  <div class="rainbow-art" role="img" aria-label="Illustration of a rainbow ending in a cloud"></div>
  <div class="brand"><span class="brand-mark"></span>Maple Nook Kidcare</div>

  <div class="panel"></div>
  <div class="hero" role="img" aria-label="Photo of four smiling children in a bright classroom"></div>

  <svg class="nav-ribbon" viewBox="0 0 1076 82" aria-hidden="true">
    <polygon points="0,30 40,30 40,80 14,80 26,55" fill="var(--nav-tail)"/>
    <polygon points="31,48 40,48 40,80" fill="var(--nav-fold)"/>
    <polygon points="1076,30 1036,30 1036,80 1062,80 1050,55" fill="var(--nav-tail)"/>
    <polygon points="1045,48 1036,48 1036,80" fill="var(--nav-fold)"/>
  </svg>
  <nav class="nav">
    <a href="#">Home</a>
    <a href="#">About Us</a>
    <a href="#">Services</a>
    <a href="#">Hours and Fees</a>
    <a href="#">Policies</a>
    <a href="#">Contact Us</a>
    <a href="#">Photos</a>
    <a href="#">Testimonials</a>
  </nav>

  <section class="intro">
    <h1>Welcome to Maple Nook Kidcare, a playspace where children can play, create, and imagine!</h1>
    <p>Welcome to Maple Nook Kidcare, a licensed Group Family Day Care, located in Brookfield's beautiful Harbor Hill. We are located on a pretty, tree-lined block on Linden Street, between Oak and Elm Avenues. We are a few blocks from the B line tram and the Park Road bus route, and we offer flexible hourly childcare, making it as easy as possible for busy parents on the go to arrange their children's care.</p>
    <p>We invite you to learn more about us and hope you will visit us soon!</p>
  </section>

  <section class="news">
    <h2>NEWS:</h2>
    <p>We are thrilled to have found a new cheerful space with a private backyard! It's large, sunny, and filled with outdoor play equipment such as a toddler slide, sand/water activity table, and lots of toys!</p>
    <p>Please stay tuned for updates on our program and services as we say goodbye to Winter and hello to Spring!</p>
  </section>

  <div class="card card-learning">
    <h3>LEARNING</h3>
    <p>We develop age-appropriate activities that introduce and strengthen academic and social skills.</p>
  </div>
  <div class="card card-creativity">
    <h3>CREATIVITY</h3>
    <p>We offer children a wide range of creative opportunities including art projects, toddler yoga lessons, afternoon tea parties, dress up play, and a large selection of books and games.</p>
  </div>
  <div class="card card-sharing">
    <h3>SHARING</h3>
    <p>We strive to include enrichment activities that extend your child's understanding of the world and their role in it. During our tea parties, for instance, we teach and emphasize good manners so that your child can learn their benefits as they grow.</p>
  </div>
  <div class="card-art art-learning" role="img" aria-label="Illustration of a child riding a giant pencil"></div>
  <div class="card-art art-creativity" role="img" aria-label="Illustration of a girl painting under a rainbow"></div>
  <div class="card-art art-sharing" role="img" aria-label="Illustration of two children sharing drawing tools"></div>

  <footer class="footer">
    <span>© Maple Nook Kidcare 2014</span>
    <a href="#">Policy</a>
  </footer>
</body>
</html>
```